Banner Ad for website hompage - Design Project

We need 4 banner ads for the homepage of a Rent a Car company based in dubai. We rent a wide range of cars but mainly deal in the affordable cars category. Our website colors are mainly red, white and black and I can send pictures of the website (attached) if you want something to compare possible design ideas with. The banners need to promote different messages and must be appealing to the end user. It must also use pictures of cars that exist in our fleet (Pls note: this is only if you are using cars in the banner ad)

The 4 banner ads needed are as follows:
1) should promote something along the lines of we have 20+ models available and reserve a car now (This banner should also have a reserve now button, not the actual button but it's design. The button will be made and coded by us)
2) should promote something along the lines of we offer personalised service and we look after each and every custoemr individually
3) we provide attractive rates based on daily, weekly, monthly and longer rental periods (should also incorporate a reserve now message)
4) Like us on quorvia and follow us on social media for additional offers and discounts (would like for this to have a like button design implemented in it which will be linked to quorvia.)

Also please not the picture file size is 940pixels by 400pixels

Finally: I also need the psd files for the banners.

```html
<!DOCTYPE html>
<html lang="en">
<head>
<meta charset="utf-8">
<title>Rent a Car – 20+ Models Available</title>
<link rel="stylesheet" href="https://fonts.googleapis.com/css2?family=Roboto+Condensed:wght@700&display=swap">
<style>
  :root {
    --black: #000000;
    --charcoal: #1c1c1c;
    --red: #e30000;
    --red-deep: #b50000;
    --white: #ffffff;
    --paper: #f2f2f2;
    --fleet-light: #9aa3ad;
    --fleet-dark: #3a3f47;
  }
  * { margin: 0; padding: 0; box-sizing: border-box; }
  html, body {
    width: 1200px;
    height: 511px;
    overflow: hidden;
    background: var(--black);
  }
  .banner {
    position: relative;
    width: 1200px;
    height: 511px;
    overflow: hidden;
    background: radial-gradient(ellipse at 55% 45%, var(--charcoal) 0%, var(--black) 65%);
  }
  .banner-art {
    position: absolute;
    inset: 0;
    width: 1200px;
    height: 511px;
  }
  .headline {
    font-family: "Roboto Condensed", "Arial Narrow", sans-serif;
    font-weight: 700;
    fill: var(--white);
    text-anchor: middle;
  }
  .headline-count { font-size: 46px; }
  .headline-label { font-size: 37px; letter-spacing: 0.3px; }
  .reserve-label {
    font-family: "Roboto Condensed", "Arial Narrow", sans-serif;
    font-weight: 700;
    font-size: 19px;
    fill: var(--red);
  }
</style>
</head>
<body>
<main class="banner">
  <svg class="banner-art" viewBox="0 0 940 400" xmlns="http://www.w3.org/2000/svg">
    <defs>
      <linearGradient id="red-sweep" x1="0" y1="0" x2="1" y2="1">
        <stop offset="0" stop-color="var(--red-deep)"/>
        <stop offset="0.55" stop-color="var(--red)"/>
        <stop offset="1" stop-color="#ff1a1a"/>
      </linearGradient>
      <linearGradient id="light-streak" x1="0" y1="0" x2="1" y2="0">
        <stop offset="0" stop-color="#ffffff" stop-opacity="0"/>
        <stop offset="0.5" stop-color="#ffffff" stop-opacity="0.22"/>
        <stop offset="1" stop-color="#ffffff" stop-opacity="0"/>
      </linearGradient>
      <linearGradient id="fleet-tone" x1="0" y1="0" x2="1" y2="1">
        <stop offset="0" stop-color="var(--fleet-light)"/>
        <stop offset="0.5" stop-color="#8a1c24"/>
        <stop offset="1" stop-color="var(--fleet-dark)"/>
      </linearGradient>
    </defs>

    <!-- light streaks -->
    <g class="streaks" fill="none" stroke="url(#light-streak)">
      <path d="M60 340 C 220 250, 420 170, 700 120" stroke-width="1.5"/>
      <path d="M90 360 C 260 270, 460 190, 760 150" stroke-width="1"/>
      <path d="M200 330 C 360 260, 520 200, 820 190" stroke-width="0.8"/>
    </g>

    <!-- red curved panel -->
    <path class="red-panel" fill="url(#red-sweep)"
      d="M0 42 L330 44 C 395 46, 440 120, 460 190 C 480 255, 505 300, 535 330
         C 430 328, 220 330, 120 318 C 50 310, 15 270, 0 215 Z"/>
    <path class="red-panel-sheen" fill="none" stroke="#ffffff" stroke-opacity="0.25" stroke-width="1.2"
      d="M20 300 C 160 240, 330 200, 520 230"/>

    <text class="headline headline-count" x="205" y="160">20+</text>
    <text class="headline headline-label" x="215" y="220">MODELS AVAILABLE</text>

    <!-- reservation form icon -->
    <g class="form-icon" transform="translate(418 168)">
      <path d="M0 4 L48 0 L54 68 L6 72 Z" fill="var(--paper)"/>
      <g stroke="#9a9a9a" stroke-width="1.2">
        <line x1="10" y1="14" x2="38" y2="12"/>
        <line x1="11" y1="25" x2="40" y2="23"/>
        <line x1="12" y1="36" x2="41" y2="34"/>
        <line x1="13" y1="47" x2="42" y2="45"/>
        <line x1="14" y1="58" x2="34" y2="57"/>
      </g>
      <path d="M30 46 L64 4 L68 7 L34 49 L28 52 Z" fill="#333"/>
      <path d="M62 6 L66 1 L70 4 L66 9 Z" fill="#777"/>
    </g>

    <!-- reserve now button -->
    <g class="reserve-button">
      <rect x="690" y="27" width="210" height="46" rx="6" fill="var(--white)"/>
      <circle cx="705" cy="52" r="31" fill="var(--white)"/>
      <g class="car-icon" fill="var(--red)" transform="translate(691 40)">
        <path d="M5 8 L8 2 C 9 0, 10 0, 12 0 L20 0 C 22 0, 23 0, 24 2 L27 8 L29 9 L29 20 L25 20 L25 17 L7 17 L7 20 L3 20 L3 9 Z"/>
        <rect x="9" y="3" width="14" height="5" fill="var(--white)"/>
        <circle cx="9" cy="12" r="2" fill="var(--white)"/>
        <circle cx="23" cy="12" r="2" fill="var(--white)"/>
      </g>
      <text class="reserve-label" x="746" y="57">RESERVE NOW</text>
    </g>

    <!-- fleet photograph area -->
    <path class="fleet-photo" role="img" aria-label="Photograph of a row of parked rental cars in silver, blue, white and red"
      fill="url(#fleet-tone)"
      d="M722 280 C 760 255, 820 225, 870 205 L 940 175 L 940 400 L 850 400 C 800 360, 760 320, 722 300 Z"/>
  </svg>
</main>
</body>
</html>
```